Wordpress Design Project (Brannock)

We need a wordpress design for an established auction and real estate company based in Minnesota. The winning design will incorporate the colors of logo (red white and black) creatively in a very professional and clean layout. Client mentions liking the site http://www.quillbrook.example/ and http://www.tarvenlodeauction.example/ as a general idea for what they like.

Industry/Entity Type

Real Estate

Requirements
Must have
• Navigation:
1) Home - will have auction list, no text
2) Upcoming Auctions
3) Online Auctions
4) Real Estate
5) Auction Gallery
6) For Sale
7) About Us
8) Contact Us

Sidebar widget will include:
- email signup
- asset for sale fader (seen in Featured Listings at http://www.tarvenlodeauction.example/)
- Slideshow - initial image attached
- Video widget (image attached)
- social media icons for Vidlark, Friendspan, Chirpel, Workloop and RSS feed
- testimonials

Footer will have smaller logo and contact info
Nice to have
• Nice to Have:
- use of drop-down menu design for 'About Us'
1) About Brannock
2) Testimonials

```html
<!DOCTYPE html>
<html lang="en">
<head>
<meta charset="utf-8">
<title>Brannock Auction &amp; Real Estate Services</title>
<link href="https://fonts.googleapis.com/css2?family=Roboto:ital,wght@0,400;0,500;0,700;1,700&display=swap" rel="stylesheet">
<style>
:root{
  --page:#a9a6a4;
  --white:#ffffff;
  --red:#a51c24;
  --red-dark:#8a1219;
  --ink:#222222;
  --text:#333333;
  --bar-top:#3a3a3a;
  --bar-bot:#111111;
  --line:#dcdcdc;
  --panel-bot:#ececec;
  --field-green:#4f8a2a;
  --field-brown:#6b5a44;
}
*{box-sizing:border-box;margin:0;padding:0}
html,body{width:858px;height:1200px;overflow:hidden}
body{background:linear-gradient(#b3b0ae,#9f9c9a);font-family:"Roboto",Arial,sans-serif;color:var(--text);position:relative}
.sheet{position:absolute;left:73px;top:21px;width:711px;height:1165px;background:var(--white);border-radius:10px 10px 0 0}
.abs{position:absolute}
/* nav */
.main-nav{position:absolute;left:77px;top:24px;width:703px;height:34px;background:linear-gradient(var(--bar-top),var(--bar-bot));display:flex;align-items:center;border-radius:4px 4px 0 0;z-index:3}
.nav-link{flex:1 1 auto;white-space:nowrap;text-align:center;color:#fff;font-size:10px;font-weight:700;text-decoration:none;height:34px;line-height:34px;padding:0 12px;border-right:1px solid #000;box-shadow:1px 0 0 #444}
.nav-link:last-child{border:0;box-shadow:none}
.nav-item{position:relative;flex:1 1 auto;height:34px;display:flex;align-items:center;justify-content:center;padding:0 6px;border-right:1px solid #000;box-shadow:1px 0 0 #444}
.nav-item .current{display:block;white-space:nowrap;background:var(--red);color:#fff;font-size:10px;font-weight:700;text-decoration:none;height:22px;line-height:22px;padding:0 10px}
.dropdown{position:absolute;left:6px;top:28px;width:88px;background:var(--red);box-shadow:0 2px 3px rgba(0,0,0,.3)}
.dropdown a{display:block;white-space:nowrap;color:#fff;font-size:9px;font-weight:500;padding:5px 9px;text-decoration:none;border-bottom:1px solid var(--red-dark)}
/* header */
.brand{position:absolute;left:77px;top:58px;width:239px;height:185px;background:linear-gradient(#f2f2f2,#e2e2e2);display:flex;flex-direction:column;align-items:center;justify-content:center;gap:10px}
.brand-name{font-size:34px;font-weight:700;color:var(--red);letter-spacing:1px;display:flex;align-items:center;gap:8px}
.brand-name i{width:16px;height:16px;background:var(--ink);display:block}
.brand-phone{font-size:14px;font-weight:700;color:var(--ink)}
.hero{position:absolute;left:316px;top:58px;width:464px;height:185px;background:linear-gradient(160deg,#3f8a2e,#5c5246 45%,#2f6f24 80%,#4b3f33)}
/* content */
.welcome h1{position:absolute;left:84px;top:269px;font-size:18px;font-weight:700;color:#333}
.welcome p{position:absolute;left:85px;top:295px;width:470px;font-size:9.2px;line-height:14.5px;color:#444}
.lot{position:absolute;left:81px;width:470px;height:168px;border:1px solid var(--line);background:linear-gradient(#fff,var(--panel-bot))}
.lot-head{position:absolute;left:4px;top:3px;width:462px;height:28px;background:linear-gradient(var(--bar-top),var(--bar-bot));color:#fff;font-size:13px;line-height:28px;padding-left:11px;box-shadow:0 2px 2px rgba(0,0,0,.3)}
.lot-photo{position:absolute;left:12px;top:47px;width:126px;height:74px;border:2px solid #ccc;background:linear-gradient(170deg,#d9d9d9 0 25%,#5aa83a 25%,var(--field-green) 55%,var(--field-brown))}
.btn-red{position:absolute;left:36px;top:129px;width:77px;height:21px;background:linear-gradient(#c12530,var(--red-dark));border-radius:3px;color:#fff;font-size:10px;font-weight:700;display:flex;align-items:center;justify-content:center;gap:5px}
.lot-info{position:absolute;left:144px;top:49px;width:315px;font-size:9.3px;line-height:13px;color:#333}
.lot-info .label{color:var(--red);font-weight:700;font-size:9.5px}
.lot-info p{text-align:justify}
/* sidebar */
.widget{position:absolute;left:573px;width:203px;border:1px solid var(--line);background:linear-gradient(#fafafa,var(--panel-bot))}
.widget-head{position:absolute;left:3px;top:3px;right:3px;height:28px;background:linear-gradient(#c01f29,var(--red-dark));color:#fff;font-size:14px;line-height:28px;padding-left:9px}
.asset-title{position:absolute;left:0;right:0;top:41px;text-align:center;color:var(--red);font-size:9.5px;font-weight:500;line-height:13px}
.asset-photo{position:absolute;left:26px;top:70px;width:150px;height:76px;border:2px solid #555;background:linear-gradient(170deg,#dcdcdc 0 25%,#5aa83a 25%,var(--field-green) 55%,var(--field-brown))}
.asset-text{position:absolute;left:0;right:0;top:153px;text-align:center;font-size:8.7px;line-height:11.5px;color:#111}
.btn-dark{position:absolute;left:67px;top:201px;width:76px;height:20px;background:linear-gradient(#444,#111);border-radius:3px;color:#fff;font-size:8.7px;line-height:20px;text-align:center}
.video{position:absolute;left:576px;top:522px;width:197px;height:141px;background:#111}
.video-screen{position:absolute;left:0;top:0;width:197px;height:128px;background:linear-gradient(#6d1a1f,#b02a32 40%,#eaeaea 40%,#dcdcdc)}
.video-title{position:absolute;left:9px;top:2px;color:#fff;font-size:8.5px;font-weight:700}
.video-bar{position:absolute;left:0;bottom:0;width:197px;height:13px;display:flex;align-items:center;gap:6px;padding:0 6px;color:#fff;font-size:6px}
.video-bar .track{flex:1;height:3px;background:#555}
.email-field{position:absolute;left:12px;top:36px;width:157px;height:22px;border:1px solid #ccc;background:#fff;font-size:8.5px;color:#999;line-height:20px;padding-left:7px}
.email-go{position:absolute;left:169px;top:36px;width:27px;height:22px;background:#111;color:#fff;font-size:11px;font-weight:700;line-height:22px;text-align:center;border-radius:0 3px 3px 0}
.email-note{position:absolute;left:15px;top:67px;width:180px;font-size:8.5px;line-height:10px;color:#222}
.quote{position:absolute;left:11px;top:44px;width:190px;font-size:9.3px;line-height:14.4px;color:#555}
.quote b{font-size:18px;color:#888;font-family:Georgia,serif;line-height:0}
.quote-by{position:absolute;right:6px;top:155px;font-size:9.3px;font-weight:700;font-style:italic;color:var(--red)}
.social{position:absolute;left:8px;top:40px;width:192px;display:flex;flex-wrap:wrap;gap:5px 4px}
.social span{display:flex;align-items:center;gap:4px;font-size:8.5px;color:#333;width:60px;white-space:nowrap}
.social i{width:12px;height:12px;border-radius:50%;background:var(--red);display:block;flex:none}
/* footer */
.site-footer{position:absolute;left:79px;top:1114px;width:700px;height:65px;background:linear-gradient(#3c3c3c,#141414);color:#fff}
.foot-brand{position:absolute;left:10px;top:22px;font-size:16px;font-weight:700;color:#ddd;display:flex;align-items:center;gap:6px}
.foot-brand i{width:10px;height:10px;background:#ddd;display:block}
.foot-info{position:absolute;right:13px;top:15px;text-align:right;font-size:8.5px;line-height:19.5px}
</style>
</head>
<body>
<div class="sheet"></div>

<nav class="main-nav">
  <a href="#" class="nav-link">Home</a>
  <a href="#" class="nav-link">Upcoming Auctions</a>
  <a href="#" class="nav-link">Online Auctions</a>
  <a href="#" class="nav-link">Real Estate</a>
  <a href="#" class="nav-link">Auction Gallery</a>
  <a href="#" class="nav-link">For Sale</a>
  <div class="nav-item">
    <a href="#" class="current">About Us</a>
    <div class="dropdown"><a href="#">About Brannock</a><a href="#">Testimonials</a></div>
  </div>
  <a href="#" class="nav-link">Contact Us</a>
</nav>

<header>
  <div class="brand">
    <div class="brand-name"><i></i>BRANNOCK</div>
    <div class="brand-phone">320-555-0147</div>
  </div>
  <div class="hero" role="img" aria-label="Crowd of bidders among green tractors at an outdoor farm auction"></div>
</header>

<section class="welcome">
  <h1>WELCOME TO BRANNOCK</h1>
  <p>Brannock dummy text of the printing and typesetting industry. Lorem Ipsum has been the industry's standard dummy text ever since the 1500s, when an unknown printer took a galley of type and scrambled it to make a type specimen book. It has survived not only five centuries,</p>
</section>

<article class="lot" style="top:358px">
  <div class="lot-head">Vehicles * Tractors * Farm Machinery</div>
  <div class="lot-photo" role="img" aria-label="Green telehandler at an auction yard"></div>
  <div class="btn-red"><svg width="10" height="10" viewBox="0 0 10 10"><circle cx="6" cy="4" r="3" fill="none" stroke="#fff" stroke-width="1.5"/><path d="M4 6 1 9" stroke="#fff" stroke-width="1.8"/></svg>Details</div>
  <div class="lot-info"><div class="label">Selling To the Highest Bidder</div><p style="margin-top:3px">simply dummy text of the printing and typesetting industry. Lorem Ipsum has been the industry's.</p><div class="label" style="margin-top:5px">Live On Site Auction</div><p>Begins:&nbsp; Saturday, March 16, 2013 at 10:00 AM EDT</p><div class="label" style="margin-top:5px">Location</div><p>2426 Old Harlow, OK 73999</p></div>
</article>

<article class="lot" style="top:548px">
  <div class="lot-head">Vehicles * Tractors * Farm Machinery</div>
  <div class="lot-photo" role="img" aria-label="Green telehandler at an auction yard"></div>
  <div class="btn-red"><svg width="10" height="10" viewBox="0 0 10 10"><circle cx="6" cy="4" r="3" fill="none" stroke="#fff" stroke-width="1.5"/><path d="M4 6 1 9" stroke="#fff" stroke-width="1.8"/></svg>Details</div>
  <div class="lot-info"><div class="label">Selling To the Highest Bidder</div><p style="margin-top:3px">simply dummy text of the printing and typesetting industry. Lorem Ipsum has been the industry's.</p><div class="label" style="margin-top:5px">Live On Site Auction</div><p>Begins:&nbsp; Saturday, March 16, 2013 at 10:00 AM EDT</p><div class="label" style="margin-top:5px">Location</div><p>2426 Old Harlow, OK 73999</p></div>
</article>

<article class="lot" style="top:738px">
  <div class="lot-head">Vehicles * Tractors * Farm Machinery</div>
  <div class="lot-photo" role="img" aria-label="Green telehandler at an auction yard"></div>
  <div class="btn-red"><svg width="10" height="10" viewBox="0 0 10 10"><circle cx="6" cy="4" r="3" fill="none" stroke="#fff" stroke-width="1.5"/><path d="M4 6 1 9" stroke="#fff" stroke-width="1.8"/></svg>Details</div>
  <div class="lot-info"><div class="label">Selling To the Highest Bidder</div><p style="margin-top:3px">simply dummy text of the printing and typesetting industry. Lorem Ipsum has been the industry's.</p><div class="label" style="margin-top:5px">Live On Site Auction</div><p>Begins:&nbsp; Saturday, March 16, 2013 at 10:00 AM EDT</p><div class="label" style="margin-top:5px">Location</div><p>2426 Old Harlow, OK 73999</p></div>
</article>

<article class="lot" style="top:927px">
  <div class="lot-head">Vehicles * Tractors * Farm Machinery</div>
  <div class="lot-photo" role="img" aria-label="Green telehandler at an auction yard"></div>
  <div class="btn-red"><svg width="10" height="10" viewBox="0 0 10 10"><circle cx="6" cy="4" r="3" fill="none" stroke="#fff" stroke-width="1.5"/><path d="M4 6 1 9" stroke="#fff" stroke-width="1.8"/></svg>Details</div>
  <div class="lot-info"><div class="label">Selling To the Highest Bidder</div><p style="margin-top:3px">simply dummy text of the printing and typesetting industry. Lorem Ipsum has been the industry's.</p><div class="label" style="margin-top:5px">Live On Site Auction</div><p>Begins:&nbsp; Saturday, March 16, 2013 at 10:00 AM EDT</p><div class="label" style="margin-top:5px">Location</div><p>2426 Old Harlow, OK 73999</p></div>
</article>

<aside>
  <div class="widget" style="top:265px;height:235px">
    <div class="widget-head" style="font-size:16px;padding-left:20px">Asset for Sale</div>
    <div class="asset-title">13.35 ACRES OF PRIME DEVELOP<br>&amp; 33RD STREET</div>
    <div class="asset-photo" role="img" aria-label="Green telehandler on a property lot"></div>
    <div class="asset-text">LOTS 13 &amp; 14 FOR SALE, MARROWFIELD<br>IOWA<br>Third Street, Marrowfield, IA 50999</div>
    <div class="btn-dark">more details...</div>
  </div>

  <div class="widget" style="top:518px;height:146px"></div>
  <div class="video">
    <div class="video-screen" role="img" aria-label="Bidder tutorial video showing the online bidding screen"></div>
    <div class="video-title">Brannock Bidder Tutorial.mp4</div>
    <svg class="abs" style="left:86px;top:49px" width="28" height="28" viewBox="0 0 28 28"><circle cx="14" cy="14" r="13" fill="rgba(0,0,0,.35)" stroke="#fff" stroke-width="1.5"/><path d="M11 8 20 14 11 20Z" fill="#fff"/></svg>
    <div class="video-bar"><span>&#9654;</span><span>00:00</span><span class="track"></span><span>00:00</span></div>
  </div>

  <div class="widget" style="top:684px;height:98px">
    <div class="widget-head" style="height:23px;line-height:23px">Email Sign-Up</div>
    <div class="email-field">Enter Your Email Address...</div>
    <div class="email-go">Go</div>
    <div class="email-note">Subscribe to Upcoming Auctions and our Free E-mail Newsletter.</div>
  </div>

  <div class="widget" style="top:802px;height:174px;left:571px;width:208px">
    <div class="widget-head" style="height:25px;line-height:25px">Client Testimonials</div>
    <div class="quote"><b>&ldquo;</b> simply dummy text of the printing and typesetting industry. Lorem Ipsum has been the text of the printingIpsum has been the text Ipsum has been the text &nbsp;and type &nbsp;setting industry. Lorem Ipsum has been the industry's standard dummy text. <b>&rdquo;</b></div>
    <div class="quote-by">By John Carrow...</div>
  </div>

  <div class="widget" style="top:994px;height:100px;left:571px;width:208px">
    <div class="widget-head" style="height:25px;line-height:25px">Client Testimonials</div>
    <div class="social"><span><i></i>Chirpel</span><span><i></i>Friendspan</span><span><i></i>Workloop</span><span><i></i>Vidlark</span><span><i></i>RSS</span></div>
  </div>
</aside>

<footer class="site-footer">
  <div class="foot-brand"><i></i>BRANNOCK</div>
  <div class="foot-info"><b>Phone:</b> 612-555-0193, <b>Email:</b> info@brannockauctions.example<br>Copyright (C) <b>BRANNOCK</b> 2013 - 2014 .&nbsp; All Rights Reserved</div>
</footer>
</body>
</html>
```